Engineering Consultant Business Card

I'm starting a new business as a high-end engineering consultant in a niche field. I've attached the jpg for my logo plus the branding guideline document that I've been following. You can see my business website here: www.tarvikworks.com
I'd like a business card that has the logo on one side, then the other side has (in any order): Tarvik Works, Inc.
Dana Whitlock
President and Chief EMC Engineer
www.tarvikworks.com
dana@tarvikworks.com
Optional: motto "We will solve your EMC problems as early as possible—ideally before they even start."
I'm not planning on including a phone number
Target Market(s)
Businesses, especially makers of electronics hardware
Industry/Entity Type
Electrical engineering
Contact Information for Business Card
Company name, my name, website, email

```html
<!DOCTYPE html>
<html lang="en">
<head>
<meta charset="utf-8">
<title>Tarvik Works – Business Card</title>
<link href="https://fonts.googleapis.com/css2?family=Fira+Sans:wght@400;600&family=Ubuntu:wght@400&display=swap" rel="stylesheet">
<style>
  :root {
    --stage-blue: #5e7bd9;
    --stage-grey: #e5e5e5;
    --navy: #243470;
    --mid-blue: #4a63bd;
    --bright-blue: #5b76d6;
    --soft-blue: #3d53a0;
    --card-white: #ffffff;
    --ink: #111111;
  }
  html, body {
    margin: 0;
    padding: 0;
    width: 1200px;
    height: 1200px;
    overflow: hidden;
  }
  .stage {
    position: relative;
    width: 1200px;
    height: 1200px;
    background: linear-gradient(to right, var(--stage-blue) 0 642px, var(--stage-grey) 642px 100%);
  }
  .card {
    position: absolute;
    left: 230px;
    width: 739px;
    height: 422px;
    display: block;
  }
  .card--front { top: 151px; }
  .card--back { top: 627px; }
  .name {
    font-family: "Fira Sans", sans-serif;
    font-weight: 600;
    font-size: 44px;
    letter-spacing: 0.5px;
  }
  .name__first { fill: var(--navy); }
  .name__last { fill: var(--bright-blue); }
  .job-title {
    font-family: "Fira Sans", sans-serif;
    font-size: 27px;
    fill: var(--ink);
  }
  .contact {
    font-family: "Ubuntu", sans-serif;
    font-size: 26px;
    fill: var(--ink);
  }
  .bracket, .icon-line {
    fill: none;
    stroke: var(--soft-blue);
    stroke-width: 2.5;
  }
  .wordmark {
    font-family: "Fira Sans", sans-serif;
    font-weight: 600;
    font-size: 72px;
    fill: var(--navy);
    letter-spacing: 2px;
  }
</style>
</head>
<body>
<main class="stage">

  <svg class="card card--front" viewBox="0 0 1189 679" aria-label="Tarvik Works, Inc. business card, contact side">
    <defs>
      <linearGradient id="wave-tone-front" x1="0" y1="0" x2="1" y2="1">
        <stop offset="0" stop-color="#243470"/>
        <stop offset="0.6" stop-color="#2c3d80"/>
        <stop offset="1" stop-color="#4a63bd"/>
      </linearGradient>
      <linearGradient id="wave-tone-back" x1="0" y1="0" x2="1" y2="1">
        <stop offset="0" stop-color="#243470"/>
        <stop offset="1" stop-color="#34479a"/>
      </linearGradient>
    </defs>
    <rect width="1189" height="679" fill="var(--card-white)"/>
    <path class="wave-area" role="img" aria-label="Decorative flowing wave band in navy and blue"
          d="M20,0 C450,30 570,200 650,380 C750,600 900,665 1189,679 L1189,0 Z"
          fill="url(#wave-tone-front)"/>

    <g class="contact-row contact-row--name">
      <line class="bracket" x1="48" y1="295" x2="48" y2="361"/>
      <polyline class="bracket" points="113,295 113,361 180,384"/>
      <circle cx="81" cy="318" r="10" fill="var(--soft-blue)"/>
      <path d="M64,340 C66,328 74,326 81,332 C88,326 96,328 98,340 C94,350 68,350 64,340 Z" fill="var(--soft-blue)"/>
      <text class="name" x="152" y="327"><tspan class="name__first">DANA</tspan> <tspan class="name__last">WHITLOCK</tspan></text>
      <text class="job-title" x="153" y="358">President and Chief EMC Engineer</text>
    </g>

    <g class="contact-row contact-row--web">
      <line class="bracket" x1="48" y1="459" x2="48" y2="518"/>
      <polyline class="bracket" points="105,459 105,518 163,537"/>
      <circle class="icon-line" cx="77" cy="488" r="16"/>
      <ellipse class="icon-line" cx="77" cy="488" rx="7" ry="16"/>
      <line class="icon-line" x1="61" y1="482" x2="93" y2="482"/>
      <line class="icon-line" x1="61" y1="494" x2="93" y2="494"/>
      <line class="icon-line" x1="77" y1="472" x2="77" y2="504"/>
      <text class="contact" x="160" y="501">www.tarvikworks.com</text>
    </g>

    <g class="contact-row contact-row--email">
      <line class="bracket" x1="48" y1="553" x2="48" y2="612"/>
      <polyline class="bracket" points="105,553 105,612 163,632"/>
      <rect class="icon-line" x="61" y="572" width="32" height="24" rx="3"/>
      <polyline class="icon-line" points="64,575 77,588 90,575"/>
      <text class="contact" x="160" y="592">dana@tarvikworks.com</text>
    </g>
  </svg>

  <svg class="card card--back" viewBox="0 0 1189 679" aria-label="Tarvik Works, Inc. business card, brand side">
    <rect width="1189" height="679" fill="var(--card-white)"/>
    <path class="wave-area wave-area--top" role="img" aria-label="Decorative wave band in navy and blue, top left"
          d="M0,0 L662,0 C420,30 330,90 285,220 C230,350 170,382 0,385 Z"
          fill="url(#wave-tone-back)"/>
    <path class="wave-area wave-area--bottom" role="img" aria-label="Decorative wave band in navy and blue, bottom right"
          d="M520,679 C800,665 900,600 960,470 C1020,340 1070,300 1189,294 L1189,679 Z"
          fill="url(#wave-tone-back)"/>
    <g class="brand-mark">
      <circle cx="345" cy="339" r="30" fill="none" stroke="var(--navy)" stroke-width="10"/>
      <text class="wordmark" x="395" y="364">TARVIK WORKS</text>
    </g>
  </svg>

</main>
</body>
</html>
```